Brindle Logistics Business Card Design

We are a trucking and warehousing company. We run freight in the US manly from the Pacific NW to TX and back up the the PNW. We also do warehousing where we store, move, and distribute freight. Looking for a clean and modern design of business card. We would like to look rich and elegant. Attached is our logo.

Industry/Entity Type

Trucking Company

Contact Information for Business Card

Looking for a clean and modern design of business card. We would like to look rich and elegant.

Font styles to use
Sans Serif

Colors

Designer to choose colors to be used in the design.

Requirements
Must have
• logo but it should not dominate the card
Should not have
• logo should not dominate the card

```html
<!DOCTYPE html>
<html lang="en">
<head>
<meta charset="utf-8">
<title>Brindle Logistics Business Card</title>
<link rel="stylesheet" href="https://fonts.googleapis.com/css2?family=Arimo:wght@300;400;700&display=swap">
<style>
  :root {
    --page: #eff0f0;
    --card: #ffffff;
    --blue: #0072bb;
    --orange: #f7941d;
    --red: #e8202a;
    --ink: #3d3d3f;
    --ink-soft: #5a5a5c;
    --pattern: #eef2f9;
    --white: #ffffff;
  }
  * { box-sizing: border-box; margin: 0; padding: 0; }
  html, body { width: 999px; height: 1200px; overflow: hidden; }
  body {
    background: var(--page);
    font-family: "Arimo", Arial, sans-serif;
    position: relative;
  }
  .card {
    position: absolute;
    left: 53px;
    width: 892px;
    height: 509px;
    background: var(--card);
    box-shadow: 4px 5px 4px rgba(0, 0, 0, 0.35);
    overflow: hidden;
  }
  .card--front { top: 47px; }
  .card--back { top: 645px; height: 507px; }

  .bar { position: absolute; background: var(--orange); }

  /* front */
  .front-bar-left { left: 0; top: 27px; width: 374px; height: 55px; }
  .front-bar-right { left: 738px; top: 84px; width: 154px; height: 55px; }
  .brackets { position: absolute; left: 0; top: 0; width: 892px; height: 341px; }

  .wordmark {
    position: absolute;
    display: flex;
    align-items: center;
    color: var(--ink);
    font-weight: 400;
    white-space: nowrap;
  }
  .wordmark__dot { border-radius: 50%; background: var(--blue); flex: none; }
  .front-wordmark { left: 420px; top: 62px; font-size: 22px; gap: 10px; }
  .front-wordmark .wordmark__dot { width: 36px; height: 36px; }

  .company {
    position: absolute;
    left: 100px;
    top: 175px;
  }
  .company__name {
    font-size: 31px;
    font-weight: 700;
    color: var(--ink);
    letter-spacing: 0.2px;
  }
  .company__tagline {
    margin-top: 3px;
    margin-left: 35px;
    font-size: 19px;
    font-weight: 300;
    color: var(--ink-soft);
    letter-spacing: 0.5px;
  }

  .contact-band {
    position: absolute;
    left: 0; top: 341px;
    width: 892px; height: 168px;
    background: var(--blue);
  }
  .contact {
    position: absolute;
    top: 14px;
    width: 260px;
    margin-left: -130px;
    text-align: center;
  }
  .contact--address { left: 157px; }
  .contact--phone { left: 447px; }
  .contact--email { left: 739px; }
  .contact__icon { display: block; margin: 0 auto; width: 88px; height: 88px; }
  .contact__label {
    margin-top: 14px;
    color: var(--white);
    font-size: 20px;
    font-weight: 700;
  }

  /* back */
  .pattern-field {
    position: absolute;
    left: 0; top: 0;
    width: 892px; height: 332px;
    background: var(--pattern);
  }
  .back-bar-left { left: 0; top: 169px; width: 153px; height: 56px; }
  .back-bar-right { left: 733px; top: 169px; width: 159px; height: 56px; }
  .back-wordmark { left: 196px; top: 166px; font-size: 44px; gap: 18px; }
  .back-wordmark .wordmark__dot { width: 62px; height: 62px; }
  .rule { position: absolute; left: 0; top: 332px; width: 892px; height: 5px; background: var(--red); }
  .info-band {
    position: absolute;
    left: 0; top: 337px;
    width: 892px; height: 170px;
    background: var(--blue);
    text-align: center;
    color: var(--white);
  }
  .info-band__web {
    margin-top: 40px;
    font-size: 35px;
    font-weight: 400;
    letter-spacing: 8px;
  }
  .info-band__address {
    margin-top: 12px;
    font-size: 22px;
    font-weight: 700;
    letter-spacing: 2px;
  }
</style>
</head>
<body>

  <section class="card card--front">
    <div class="bar front-bar-left"></div>
    <div class="bar front-bar-right"></div>

    <div class="wordmark front-wordmark"><span class="wordmark__dot"></span>Brindle Logistics, LLC</div>

    <svg class="brackets" viewBox="0 0 892 341" fill="none" stroke="var(--red)" stroke-width="4">
      <polyline points="0,173 82,173"/>
      <polyline points="155,141 82,141 82,206"/>
      <polyline points="447,197 447,262 382,262"/>
      <polyline points="447,231 892,231"/>
    </svg>

    <div class="company">
      <p class="company__name">Brindle Logistics,LLC</p>
      <p class="company__tagline">Trucking and Warehousing</p>
    </div>

    <div class="contact-band">
      <div class="contact contact--address">
        <svg class="contact__icon" viewBox="0 0 88 88">
          <circle cx="44" cy="44" r="41" fill="none" stroke="var(--white)" stroke-width="4"/>
          <path d="M44 20 L68 44 L61 44 L61 64 L50 64 L50 51 L38 51 L38 64 L27 64 L27 44 L20 44 Z" fill="var(--orange)"/>
        </svg>
        <p class="contact__label">Company Address</p>
      </div>
      <div class="contact contact--phone">
        <svg class="contact__icon" viewBox="0 0 88 88">
          <circle cx="44" cy="44" r="41" fill="none" stroke="var(--white)" stroke-width="4"/>
          <path d="M30 22 C26 22 22 26 22 31 C23 50 38 65 57 66 C62 66 66 62 66 58 L66 55 L55 50 L50 56 C43 53 35 45 32 38 L38 33 L33 22 Z" fill="var(--orange)"/>
        </svg>
        <p class="contact__label">Company Phone</p>
      </div>
      <div class="contact contact--email">
        <svg class="contact__icon" viewBox="0 0 88 88">
          <circle cx="44" cy="44" r="41" fill="none" stroke="var(--white)" stroke-width="4"/>
          <rect x="20" y="29" width="48" height="32" rx="2" fill="var(--orange)"/>
          <polyline points="21,31 44,49 67,31" fill="none" stroke="var(--blue)" stroke-width="2.5"/>
        </svg>
        <p class="contact__label">Company email</p>
      </div>
    </div>
  </section>

  <section class="card card--back">
    <div class="pattern-field" role="img" aria-label="Faint light-blue geometric maze pattern background"></div>
    <div class="bar back-bar-left"></div>
    <div class="bar back-bar-right"></div>
    <div class="wordmark back-wordmark"><span class="wordmark__dot"></span>Brindle Logistics, LLC</div>
    <div class="rule"></div>
    <div class="info-band">
      <p class="info-band__web">www.website.com</p>
      <p class="info-band__address">company address</p>
    </div>
  </section>

</body>
</html>
```